Creative Business Card

Were looking for a new fresh and creative look to our Business card. Our company name is InkVale. Be creative, Were attaching our logo and our base colors, but your free to do anything. Name, title, Phone

Industry/Entity Type

Business

```html
<!DOCTYPE html>
<html lang="en">
<head>
<meta charset="utf-8">
<title>InkVale Business Card</title>
<link href="https://fonts.googleapis.com/css2?family=Open+Sans:wght@400;600;700;800&display=swap" rel="stylesheet">
<style>
  :root {
    --backdrop: #adabab;
    --label: #2a2a2a;
    --card-black: #121212;
    --brand-blue: #0a74bb;
    --brand-green: #7dbf42;
    --text-white: #ffffff;
    --text-dark: #111111;
  }
  html, body {
    margin: 0;
    padding: 0;
    width: 1200px;
    height: 900px;
    overflow: hidden;
    background: var(--backdrop);
    font-family: "Open Sans", Arial, sans-serif;
  }
  .stage {
    position: relative;
    width: 1200px;
    height: 900px;
  }
  .side-label {
    position: absolute;
    top: 236px;
    width: 200px;
    margin-left: -100px;
    text-align: center;
    font-size: 30px;
    font-weight: 400;
    color: var(--label);
    letter-spacing: 0.5px;
  }
  .side-label--back { left: 369px; }
  .side-label--front { left: 831px; }

  .card {
    position: absolute;
    width: 442px;
    height: 259px;
    border-radius: 18px;
    overflow: hidden;
    background: var(--card-black);
    box-shadow: 3px 5px 8px rgba(0, 0, 0, 0.45);
  }
  .card--back { left: 150px; top: 314px; }
  .card--front { left: 613px; top: 311px; }

  .card__shapes {
    position: absolute;
    inset: 0;
    width: 442px;
    height: 259px;
  }
  .shape-blue { fill: var(--brand-blue); }
  .shape-green { fill: var(--brand-green); }
  .shape-line { fill: none; stroke: #0b2a40; stroke-width: 1.5; }

  .wordmark {
    position: absolute;
    margin: 0;
    font-weight: 800;
    color: var(--brand-green);
    line-height: 1;
    white-space: nowrap;
  }
  .card--back .wordmark {
    left: 0;
    width: 442px;
    top: 103px;
    text-align: center;
    font-size: 50px;
    letter-spacing: 1px;
  }
  .card--front .wordmark {
    right: 25px;
    top: 60px;
    font-size: 36px;
    letter-spacing: 1px;
  }

  .website-pill {
    position: absolute;
    left: 0;
    width: 442px;
    top: 206px;
    text-align: center;
    font-size: 16px;
    font-weight: 700;
    color: var(--text-dark);
  }

  .person {
    position: absolute;
    left: 39px;
    top: 60px;
  }
  .person__name {
    margin: 0;
    font-size: 16px;
    font-weight: 700;
    color: var(--brand-blue);
    line-height: 1.1;
  }
  .person__title {
    margin: 0;
    font-size: 12.5px;
    color: var(--text-white);
    line-height: 1.3;
  }

  .contact-list {
    position: absolute;
    left: 38px;
    top: 129px;
    margin: 0;
    padding: 0;
    list-style: none;
  }
  .contact-list li {
    display: flex;
    align-items: center;
    height: 13.6px;
    font-size: 12.5px;
    color: var(--text-white);
  }
  .contact-icon {
    width: 12px;
    height: 10px;
    margin-right: 10px;
    display: flex;
    align-items: center;
    justify-content: center;
    color: var(--brand-green);
    font-size: 9px;
  }
  .contact-icon svg { width: 10px; height: 10px; fill: var(--brand-green); }
</style>
</head>
<body>
<main class="stage">
  <div class="side-label side-label--back">BACK</div>
  <div class="side-label side-label--front">FRONT</div>

  <section class="card card--back" aria-label="Card back">
    <svg class="card__shapes" viewBox="0 0 442 259" aria-hidden="true">
      <path class="shape-blue" d="M0 0 H263 C246 22 238 43 203 43 H0 Z"/>
      <path class="shape-blue" d="M0 184 H72 C95 184 92 243 145 243 H297 C350 243 347 184 370 184 H442 V259 H0 Z"/>
      <path class="shape-line" d="M78 190 C98 196 100 240 148 240 H294 C342 240 344 196 364 190"/>
      <path class="shape-green" d="M108 199 H334 C348 199 355 210 355 218 C355 228 345 236 330 236 H112 C97 236 88 228 88 219 C88 210 96 199 108 199 Z"/>
    </svg>
    <p class="wordmark">INKVALE</p>
    <div class="website-pill">www.yourwebsite.com</div>
  </section>

  <section class="card card--front" aria-label="Card front">
    <svg class="card__shapes" viewBox="0 0 442 259" aria-hidden="true">
      <path class="shape-blue" d="M0 0 H442 V26 H262 C238 26 232 44 200 44 H0 Z"/>
      <path class="shape-green" d="M250 6 H432 C438 6 442 11 442 16 V26 H232 C237 13 242 6 250 6 Z"/>
      <path class="shape-green" d="M0 211 H262 C282 211 290 228 306 245 H0 Z"/>
      <path class="shape-blue" d="M0 245 H268 C300 245 300 211 332 211 H442 V259 H0 Z"/>
    </svg>
    <div class="person">
      <p class="person__name">Your Name</p>
      <p class="person__title">Your title</p>
    </div>
    <p class="wordmark">INKVALE</p>
    <ul class="contact-list">
      <li><span class="contact-icon"><svg viewBox="0 0 10 10"><path d="M1 4 C1 2 3 1.5 5 1.5 C7 1.5 9 2 9 4 L7.5 4.5 L7 3.5 H3 L2.5 4.5 Z M2.5 5 H7.5 L8.5 8.5 H1.5 Z"/></svg></span>0123 456 789</li>
      <li><span class="contact-icon"><svg viewBox="0 0 10 10"><path d="M3 0.5 H7 V9.5 H3 Z M3.8 1.5 V7.5 H6.2 V1.5 Z"/></svg></span>0123 456 789</li>
      <li><span class="contact-icon">Fx</span>0123 456 789</li>
      <li><span class="contact-icon"><svg viewBox="0 0 10 10"><path d="M0.5 2 H9.5 V8 H0.5 Z M1.2 2.6 L5 5.4 L8.8 2.6 Z"/></svg></span>youremail@mail.com</li>
      <li><span class="contact-icon"><svg viewBox="0 0 10 10"><path d="M5 0.5 A4.5 4.5 0 1 0 5.01 0.5 Z M5 1.5 A3.5 3.5 0 1 1 4.99 1.5 Z M1.5 4.5 H8.5 V5.5 H1.5 Z M4.5 1.5 H5.5 V8.5 H4.5 Z"/></svg></span>www.yourwebdite.com</li>
    </ul>
  </section>
</main>
</body>
</html>
```